A start-up named "Corvath Therapeutics" - needs a new PowerPoint design

We need a new PowerPoint Design for an early-stage start-up named "Corvath Therapeutics" seeking to disrupt the current approach towards drug discovery within aging disorders.

We would like to build on Corvath's legacy, the founder of the modern science of genetics, by employing a multidisciplinary approach, experimenting, and providing elderly patients the attention they deserve.

We have selected the suffix "therapeutics" intentionally as it stands for (a medicine) the treatment of disease; the science of healing. Alzheimer’s treatment is a huge, urgent, unmet need:
- Shift from a disease-management system to a preventive medicine system
- Focus on increasing the health span, not only the life span

Target Market(s)

Pharma/ Biotech Executives Medical Institutions Healthcare professionals (MDs, nurses, payors, pharmacists, etc.) Patients

Industry/Entity Type

Healthcare

Other font styles liked:
• Celias

Colors
0054AA
0677BA
7BADD7
CADEEF
E8F1F8
E54698
E96AAD
F1A4CE
F9D9EA
FCEFF6
A7469A
B969AE
D3A5CF
EDDBEB
F8F0F9
6B429C
8869AF
B7A5CE
E3DAEB
F3F0F8

Requirements
Must have
• - differentiate from other companies named after Corvath - differentiate from other Pharma/ Biotech companies
Nice to have
• simplicity/ minimalist logo vivid colors gradient 3D Life-Sciences inspired Simple geometry Balance
Should not have
• mascot/ emblem watermark logo animated ink style nature-inspired inventive typography artistic chaos

```html
<!DOCTYPE html>
<html lang="en">
<head>
<meta charset="utf-8">
<title>Corvath Therapeutics – Presentation Template</title>
<link rel="stylesheet" href="https://fonts.googleapis.com/css2?family=Montserrat:wght@500;600&family=Poppins:wght@400;500&display=swap">
<style>
:root{
  --blue:#13a2e8;
  --blue-deep:#1c86db;
  --purple:#6a1b8f;
  --purple-mid:#5a2aa0;
  --ink:#222228;
  --black:#000;
  --white:#fff;
  --footer-purple:#6a2aa8;
  --grad-h:linear-gradient(90deg,#1890e0 0%,#3f4fc0 55%,#6a1b8f 100%);
  --grad-text:linear-gradient(90deg,#1e67c7 0%,#5a2aa0 60%,#6a1b8f 100%);
}
*{box-sizing:border-box;margin:0;padding:0}
html,body{width:1200px;height:3369px;overflow:hidden;background:var(--white)}
body{position:relative;font-family:"Poppins",sans-serif}
.slide{position:absolute;left:49px;width:1099px;height:618px;overflow:hidden;box-shadow:0 0 14px rgba(200,150,210,.35)}
.slide--cover{top:47px;background:var(--white)}
.slide--chromosome{top:702px;background:var(--grad-h)}
.slide--helix{top:1357px;background:var(--blue)}
.slide--stats{top:2012px;background:var(--grad-h)}
.slide--thanks{top:2668px;background:var(--white)}
.shapes{position:absolute;inset:0;width:100%;height:100%}
.abs{position:absolute}
.brand{position:absolute;font-family:"Montserrat",sans-serif;font-weight:500;line-height:1}
.brand .name{display:block;font-size:38px}
.brand .suffix{display:block;font-size:17px;letter-spacing:2px;margin-top:2px}
.brand--small .name{font-size:27px}
.brand--small .suffix{font-size:12px;letter-spacing:1.6px}
.brand--dark{color:#3a3ab0}
.brand--light{color:var(--white)}
.brand--right{text-align:left}
.title{position:absolute;font-family:"Montserrat",sans-serif;font-weight:500;font-size:42px;line-height:53px}
.title--grad span.g{background:var(--grad-text);-webkit-background-clip:text;background-clip:text;color:transparent}
.title--light{color:var(--white)}
.copy{position:absolute;font-size:11.5px;line-height:17.5px;color:var(--white)}
.subhead{position:absolute;font-family:"Montserrat",sans-serif;font-weight:600;font-size:14.5px;color:var(--white)}
.bullets{position:absolute;list-style:none;font-size:10.5px;line-height:13.5px;color:var(--white);width:395px}
.bullets li{position:relative;padding-left:14px;margin-bottom:13px}
.bullets li::before{content:"";position:absolute;left:0;top:2px;border-left:7px solid #e0207a;border-top:5px solid transparent;border-bottom:5px solid transparent}
.footer{position:absolute;left:37px;top:590px;font-size:11.5px;font-weight:500;color:var(--footer-purple);white-space:nowrap}
.footer .sep{margin:0 16px}
.rule{position:absolute;height:1px;top:599px}
.photo{position:absolute}
.stat{position:absolute;width:94px;height:94px}
.stat text{font-family:"Montserrat",sans-serif;font-size:21px;font-weight:500}
.contact{position:absolute;display:flex;gap:14px;font-size:12.5px;line-height:21px;color:#4a2a9a}
.contact .label{color:#5a3aa8}
.contact svg{flex:none;width:37px;height:37px}
</style>
</head>
<body>

<!-- Cover -->
<section class="slide slide--cover">
  <svg class="shapes" viewBox="0 0 834 469" preserveAspectRatio="none" aria-hidden="true">
    <defs>
      <linearGradient id="cv-frame" x1="0" x2="1"><stop offset="0" stop-color="#1890e0"/><stop offset="1" stop-color="#6a1b8f"/></linearGradient>
    </defs>
    <rect x="353" y="0" width="481" height="439" fill="url(#cv-frame)"/>
    <polygon points="293,0 353,0 470,250 420,250" fill="#1890e0"/>
    <polygon points="300,58 350,58 478,280 430,280" fill="#2a5cc4"/>
    <polygon points="680,409 834,409 834,439 668,439" fill="var(--purple)"/>
    <polygon points="664,439 834,439 834,469 648,469" fill="var(--blue)"/>
  </svg>
  <svg class="photo" style="left:0;top:0;width:1099px;height:618px" viewBox="0 0 834 469" preserveAspectRatio="none" role="img" aria-label="Photo of a scientist in a lab coat and hair cap looking into a microscope">
    <defs><linearGradient id="cv-photo" x1="0" y1="0" x2="1" y2="1"><stop offset="0" stop-color="#eef4fb"/><stop offset=".5" stop-color="#9cc4e6"/><stop offset="1" stop-color="#3f7fc8"/></linearGradient></defs>
    <polygon points="353,23 804,23 804,409 676,409 660,469 435,469 470,280 360,60" fill="url(#cv-photo)"/>
  </svg>
  <div class="brand brand--dark" style="left:37px;top:44px"><span class="name">Corvath</span><span class="suffix">Therapeutics</span></div>
  <h1 class="title title--grad" style="left:37px;top:262px"><span class="g">Neque porro<br>quisquam est qui</span><br><span style="color:var(--ink);display:inline-block;margin-top:12px">dolorem ipsum</span></h1>
  <p class="footer">www.CorvathTherapeutics.com<span class="sep">|</span>+0100 555 0148</p>
  <div class="rule" style="left:373px;width:300px;background:#8a7ab0"></div>
</section>

<!-- Chromosome -->
<section class="slide slide--chromosome">
  <svg class="shapes" viewBox="0 0 834 469" preserveAspectRatio="none" aria-hidden="true">
    <defs><linearGradient id="ch-block" x1="0" x2="1"><stop offset="0" stop-color="#1a96e4"/><stop offset="1" stop-color="#6a1b8f"/></linearGradient></defs>
    <rect x="646" y="0" width="188" height="469" fill="url(#ch-block)"/>
    <rect x="618" y="34" width="28" height="435" fill="var(--blue)"/>
  </svg>
  <svg class="photo" style="left:484px;top:100px;width:538px;height:416px" viewBox="0 0 538 416" preserveAspectRatio="none" role="img" aria-label="3D illustration of chromosomes floating over a DNA strand">
    <defs><radialGradient id="ch-photo" cx=".6" cy=".45" r=".7"><stop offset="0" stop-color="#f3d6ec"/><stop offset=".45" stop-color="#9fd8ee"/><stop offset="1" stop-color="#3fa6d8"/></radialGradient></defs>
    <rect x="1" y="1" width="536" height="414" fill="url(#ch-photo)" stroke="#fff" stroke-width="2"/>
  </svg>
  <div class="brand brand--light brand--small" style="left:37px;top:28px"><span class="name">Corvath</span><span class="suffix">Therapeutics</span></div>
  <h2 class="title title--light" style="left:37px;top:90px">Neque porro<br>quisquam est qui</h2>
  <p class="copy" style="left:37px;top:220px;width:400px">Sed ut perspiciatis unde omnis iste natus error sit voluptatem accusantium doloremque laudantium, totam rem aperiam, eaque ipsa quae ab illo inventore veritatis et quasi architecto beatae vitae dicta sunt explicabo.</p>
  <h3 class="subhead" style="left:37px;top:305px">Nemo enim ipsam voluptatem quia voluptas</h3>
  <ul class="bullets" style="left:37px;top:339px">
    <li>Sed ut perspiciatis unde omnis iste natus error sit voluptatem</li>
    <li>Doloremque laudantium, totam rem aperiam, eaque ipsa quae ab illo inventore veritatis et quasi architecto</li>
    <li>Beatae vitae dicta sunt explicabo.</li>
    <li>Sed ut perspiciatis unde omnis iste natus error sit voluptatem</li>
    <li>Doloremque laudantium, totam rem aperiam, eaque ipsa quae ab illo inventore veritatis et quasi architecto</li>
    <li>Beatae vitae dicta sunt explicabo.</li>
  </ul>
  <p class="footer">www.CorvathTherapeutics.com<span class="sep">|</span>+0100 555 0148</p>
  <div class="rule" style="left:373px;width:687px;background:rgba(255,255,255,.45)"></div>
</section>

<!-- Helix -->
<section class="slide slide--helix">
  <svg class="shapes" viewBox="0 0 834 469" preserveAspectRatio="none" aria-hidden="true">
    <polygon points="0,409 272,409 258,439 0,439" fill="var(--purple)"/>
    <polygon points="505,58 552,58 318,409 268,409" fill="var(--purple)"/>
    <polygon points="540,0 834,0 834,469 298,469" fill="var(--black)"/>
  </svg>
  <svg class="photo" style="left:0;top:0;width:1099px;height:618px" viewBox="0 0 834 469" preserveAspectRatio="none" role="img" aria-label="Close-up illustration of a glowing red DNA double helix on a dark bokeh background">
    <defs><linearGradient id="hx-photo" x1="0" y1="0" x2="1" y2="1"><stop offset="0" stop-color="#2a3050"/><stop offset=".45" stop-color="#c2204a"/><stop offset="1" stop-color="#3a2a55"/></linearGradient></defs>
    <polygon points="29,23 482,23 220,404 29,404" fill="url(#hx-photo)"/>
  </svg>
  <div class="brand brand--small" style="right:44px;top:40px;color:#5a5ae0"><span class="name">Corvath</span><span class="suffix">Therapeutics</span></div>
  <h2 class="title" style="right:58px;top:160px;text-align:right"><span style="color:var(--blue)">Quisquam est qui</span><br><span style="color:var(--white)">dolorem ipsum</span></h2>
  <div class="copy" style="left:575px;top:285px;width:469px;font-size:11px;line-height:20.7px;text-align:justify">
    <p>Sed ut perspiciatis unde omnis iste natus error sit voluptatem accusantium doloremque laudantium, totam rem aperiam, eaque ipsa quae ab illo inventore veritatis et quasi architecto beatae vitae dicta sunt explicabo. Nemo enim ipsam voluptatem quia voluptas sit aspernatur aut odit aut fugit, sed quia consequuntur magni dolores eos qui ratione voluptatem sequi nesciunt. Neque porro quisquam est, qui dolorem ipsum quia dolor sit amet, consectetur, adipisci velit, sed quia non numquam eius modi tempora incidunt ut labore et dolore.</p>
    <p style="margin-top:20px;text-align-last:right">Ut enim ad minima veniam, quis nostrum exercitationem ullam corporis suscipit laboriosam, nisi ut aliquid ex ea commodi consequatur? Quis autem vel eum iure reprehenderit qui in ea voluptate velit esse quam nihil molestiae consequatur, vel illum qui dolorem eum fugiat quo voluptas nulla pariatur?</p>
  </div>
  <p class="footer">www.CorvathTherapeutics.com<span class="sep">|</span>+0100 555 0148</p>
  <div class="rule" style="left:420px;width:640px;background:rgba(255,255,255,.35)"></div>
</section>

<!-- Stats -->
<section class="slide slide--stats">
  <svg class="shapes" viewBox="0 0 834 469" preserveAspectRatio="none" aria-hidden="true">
    <defs><linearGradient id="st-block" x1="0" x2="1"><stop offset="0" stop-color="#1a96e4"/><stop offset="1" stop-color="#6a1b8f"/></linearGradient></defs>
    <rect x="646" y="0" width="188" height="469" fill="url(#st-block)"/>
    <rect x="618" y="34" width="28" height="435" fill="var(--blue)"/>
  </svg>
  <svg class="photo" style="left:484px;top:100px;width:538px;height:416px" viewBox="0 0 538 416" preserveAspectRatio="none" role="img" aria-label="Photo of a pile of colourful capsules and pills on a navy background">
    <defs><radialGradient id="st-photo" cx=".5" cy=".5" r=".6"><stop offset="0" stop-color="#2a3a8a"/><stop offset="1" stop-color="#1a2468"/></radialGradient></defs>
    <rect width="538" height="416" fill="url(#st-photo)"/>
  </svg>
  <div class="brand brand--light brand--small" style="left:37px;top:28px"><span class="name">Corvath</span><span class="suffix">Therapeutics</span></div>
  <h2 class="title title--light" style="left:37px;top:90px">Neque porro<br>quisquam est qui</h2>
  <p class="copy" style="left:37px;top:220px;width:400px">Sed ut perspiciatis unde omnis iste natus error sit voluptatem accusantium doloremque laudantium, totam rem aperiam</p>
  <h3 class="subhead" style="left:37px;top:269px">Nemo enim ipsam voluptatem quia voluptas</h3>
  <ul class="bullets" style="left:37px;top:302px">
    <li>Sed ut perspiciatis unde omnis iste natus error sit voluptatem</li>
    <li>Doloremque laudantium, totam rem aperiam, eaque ipsa quae ab illo inventore veritatis et quasi architecto</li>
  </ul>
  <svg class="stat" style="left:41px;top:402px" viewBox="0 0 94 94" role="img" aria-label="65 percent">
    <circle cx="47" cy="47" r="42" fill="none" stroke="#2a8ae0" stroke-width="7"/>
    <circle cx="47" cy="47" r="42" fill="none" stroke="#3a1a8a" stroke-width="7" stroke-dasharray="171.5 264" transform="rotate(-90 47 47)"/>
    <text x="47" y="55" text-anchor="middle" fill="#4a1a9a">65%</text>
  </svg>
  <svg class="stat" style="left:180px;top:402px" viewBox="0 0 94 94" role="img" aria-label="85 percent">
    <circle cx="47" cy="47" r="42" fill="none" stroke="#3a6ad0" stroke-width="7"/>
    <circle cx="47" cy="47" r="42" fill="none" stroke="var(--blue)" stroke-width="7" stroke-dasharray="224 264" transform="rotate(-90 47 47)"/>
    <text x="47" y="55" text-anchor="middle" fill="var(--blue)">85%</text>
  </svg>
  <svg class="stat" style="left:318px;top:402px" viewBox="0 0 94 94" role="img" aria-label="95 percent">
    <circle cx="47" cy="47" r="42" fill="none" stroke="#5a4ac0" stroke-width="7"/>
    <circle cx="47" cy="47" r="42" fill="none" stroke="#7a1a8a" stroke-width="7" stroke-dasharray="251 264" transform="rotate(-90 47 47)"/>
    <text x="47" y="55" text-anchor="middle" fill="#7a1a8a">95%</text>
  </svg>
  <p class="footer">www.CorvathTherapeutics.com<span class="sep">|</span>+0100 555 0148</p>
  <div class="rule" style="left:373px;width:687px;background:rgba(255,255,255,.45)"></div>
</section>

<!-- Thank you -->
<section class="slide slide--thanks">
  <svg class="shapes" viewBox="0 0 834 469" preserveAspectRatio="none" aria-hidden="true">
    <defs><linearGradient id="ty-band" x1="0" x2="1"><stop offset="0" stop-color="#1a86dc"/><stop offset="1" stop-color="#6a1b8f"/></linearGradient></defs>
    <rect x="0" y="0" width="193" height="469" fill="url(#ty-band)"/>
    <rect x="193" y="32" width="29" height="437" fill="var(--blue)"/>
  </svg>
  <svg class="photo" style="left:82px;top:100px;width:538px;height:416px" viewBox="0 0 538 416" preserveAspectRatio="none" role="img" aria-label="Photo of a gloved hand holding a petri dish with blue liquid beside a well plate">
    <defs><linearGradient id="ty-photo" x1="0" y1="0" x2="1" y2="1"><stop offset="0" stop-color="#1a2a4a"/><stop offset=".45" stop-color="#6aa6d8"/><stop offset="1" stop-color="#e4eef8"/></linearGradient></defs>
    <rect width="538" height="416" fill="url(#ty-photo)"/>
  </svg>
  <div class="brand brand--dark brand--small" style="right:40px;top:28px"><span class="name">Corvath</span><span class="suffix">Therapeutics</span></div>
  <h2 class="title title--grad" style="left:645px;top:148px"><span class="g">Thank You!<br>quisquam est qui</span></h2>
  <p class="copy" style="left:645px;top:277px;width:400px;color:#3a3a48">Sed ut perspiciatis unde omnis iste natus error sit voluptatem accusantium doloremque laudantium, totam rem aperiam</p>
  <div class="contact" style="left:645px;top:346px">
    <svg viewBox="0 0 37 37" aria-hidden="true"><circle cx="18.5" cy="18.5" r="16.5" fill="none" stroke="#4a2a9a" stroke-width="1.8"/><path d="M13 11.5l3 -0.5 1.6 4 -2 1.4c.9 2 2.4 3.5 4.4 4.4l1.4-2 4 1.6-.5 3c-6.5.3-12.2-5.4-11.9-11.9z" fill="none" stroke="#4a2a9a" stroke-width="1.6" stroke-linejoin="round"/></svg>
    <div><div class="label">Phone:</div>+0100 555 0148</div>
  </div>
  <div class="contact" style="left:844px;top:346px">
    <svg viewBox="0 0 37 37" aria-hidden="true"><circle cx="18.5" cy="18.5" r="16.5" fill="none" stroke="#4a2a9a" stroke-width="1.8"/><rect x="11" y="13" width="15" height="11" rx="1.5" fill="none" stroke="#4a2a9a" stroke-width="1.6"/><path d="M11.5 14l7 5.5 7-5.5" fill="none" stroke="#4a2a9a" stroke-width="1.6"/></svg>
    <div><div class="label">Email:</div>hello@corvath-tx.com</div>
  </div>
  <div class="contact" style="left:645px;top:425px">
    <svg viewBox="0 0 37 37" aria-hidden="true"><circle cx="18.5" cy="18.5" r="16.5" fill="none" stroke="#4a2a9a" stroke-width="1.8"/><path d="M18.5 28s-6-6.5-6-11a6 6 0 0 1 12 0c0 4.5-6 11-6 11z" fill="none" stroke="#4a2a9a" stroke-width="1.6"/><circle cx="18.5" cy="17" r="2.2" fill="none" stroke="#4a2a9a" stroke-width="1.6"/></svg>
    <div>1180 Larkspur Ridge Rd<br>Suite 300 Dunmore, Or 97000</div>
  </div>
  <div class="rule" style="left:292px;width:768px;background:#9a8ab8"></div>
</section>

</body>
</html>
```